Silver Brook Home Business Cards

We need Business cards development for our expanding business. Our Company SilverBrookHome promotes grain free living through products, services and healthy living concepts. Our Products are:
Non-Grain
Non- GMO
Non- Soy
Gluten-Free

Project Deadline Extended
Reason: We will need to extend the deadline on our Business Card contest. Thanks, SBH

```html
<!DOCTYPE html>
<html lang="en">
<head>
<meta charset="utf-8">
<title>Silver Brook Home – Business Card</title>
<link rel="stylesheet" href="https://fonts.googleapis.com/css2?family=Open+Sans:ital,wght@0,400;0,600;1,400&family=PT+Serif&display=swap">
<style>
  :root {
    --stage: #3a3a3a;
    --card-white: #ffffff;
    --band-top: #34a300;
    --band-mid: #7fcf52;
    --band-fade: #ffffff;
    --brand-green: #2f7d0c;
    --accent-green: #49b800;
    --ink: #1e2a14;
    --rule: #e4e6e2;
  }
  html, body {
    margin: 0;
    width: 1200px;
    height: 1062px;
    overflow: hidden;
    background: var(--stage);
  }
  .stage {
    position: relative;
    width: 1200px;
    height: 1062px;
  }
  .card {
    position: absolute;
    left: 63px;
    top: 224px;
    width: 537px;
    height: 307px;
    transform: scale(2);
    transform-origin: 0 0;
    background: var(--card-white);
    overflow: hidden;
    font-family: "Open Sans", sans-serif;
    color: var(--ink);
    box-shadow: 0 2px 6px rgba(0,0,0,.35);
  }
  .brand-bar {
    position: absolute;
    left: 0; top: 0;
    width: 100%;
    height: 82px;
    background: var(--card-white);
  }
  .brand-rule {
    position: absolute;
    left: 0; top: 82px;
    width: 100%;
    height: 8px;
    background: linear-gradient(var(--card-white), var(--rule));
  }
  .brand {
    position: absolute;
    left: 0; right: 0; top: 26px;
    display: flex;
    align-items: center;
    justify-content: center;
    gap: 8px;
  }
  .brand-dot {
    width: 22px; height: 22px;
    border-radius: 50%;
    background: var(--accent-green);
  }
  .brand-name {
    font-weight: 600;
    font-size: 30px;
    letter-spacing: -0.8px;
    color: var(--brand-green);
    line-height: 1;
  }
  .info-band {
    position: absolute;
    left: 0; top: 90px;
    width: 100%;
    height: 217px;
    background: linear-gradient(to bottom, var(--band-top) 0%, var(--band-mid) 45%, var(--band-fade) 85%);
  }
  .emblem-area {
    position: absolute;
    left: 168px; top: 126px;
    width: 120px; height: 120px;
    border-radius: 50%;
    background: radial-gradient(circle, rgba(255,255,255,.16), rgba(255,255,255,0) 70%);
  }
  .person {
    position: absolute;
    left: 18px; top: 147px;
    width: 115px;
    text-align: center;
    font-family: "PT Serif", serif;
    color: #2b3520;
  }
  .person-name { font-size: 18px; line-height: 26px; }
  .person-title { font-size: 22px; line-height: 28px; }
  .contact {
    position: absolute;
    right: 17px; top: 110px;
    text-align: right;
    font-size: 16px;
    line-height: 23.6px;
    margin: 0;
    padding: 0;
    list-style: none;
  }
  .product-line {
    position: absolute;
    left: 30px; top: 269px;
    width: 449px;
    display: flex;
    align-items: center;
    justify-content: space-between;
    font-size: 14px;
    font-style: italic;
    color: #2d3a22;
  }
  .product-mark {
    width: 9px; height: 9px;
    border-radius: 50%;
    background: var(--brand-green);
  }
</style>
</head>
<body>
<main class="stage">
  <article class="card">
    <header class="brand-bar">
      <div class="brand">
        <span class="brand-dot"></span>
        <span class="brand-name">SilverBrookHome</span>
      </div>
    </header>
    <div class="brand-rule"></div>
    <section class="info-band"></section>
    <div class="emblem-area" role="img" aria-label="Soft decorative glow behind the contact details"></div>
    <div class="person">
      <div class="person-name">Name</div>
      <div class="person-title">Title Here</div>
    </div>
    <ul class="contact">
      <li>Address 1</li>
      <li>Address 22</li>
      <li>Address 333</li>
      <li>123456789012345678</li>
      <li>sbh@sbh.com</li>
      <li>www.sbh.com</li>
    </ul>
    <div class="product-line">
      <span class="product-mark"></span><span>Non - Grain</span>
      <span class="product-mark"></span><span>Non - GMO</span>
      <span class="product-mark"></span><span>Non - Soy</span>
      <span class="product-mark"></span><span>Gluten - Free</span>
      <span class="product-mark"></span>
    </div>
  </article>
</main>
</body>
</html>
```